Business Card Design

Brantock Energy, L.P. is an energy and lifecycle management firm that creates value in petroleum products through synergistic marketing, trading, recovery, logistics and beneficial reuse services.

Sell top-quality refinery feedstock, petroleum products and co-products on the spot and futures makets (energy trading)

Separate, reclaim and/or manufacture valuable products for beneficial reuse (environmental)
Updates

The tag line Understanding Solutions   Performance are three different concepts and need to be kept either spaced apart or separated in some way. Thanks. 

Target Market(s)

Refiners, Petroleum storage companies, energy marketers

Industry/Entity Type

Business

Contact Information for Business Card

Glenda M. Holloway
Principal
Brantock Energy, L.P.
4817 Quimby St.
Houston, TX 77310
713-482-6159 phone
713-624-8841 fax
g.holloway@brantockenergy-example.com
www.brantockenergy-example.com

Requirements
Must have
• Tagline outlined in matching orange -

Understanding Solutions Performance
Nice to have
• Coordinating typestyles

```html
<!DOCTYPE html>
<html lang="en">
<head>
<meta charset="utf-8">
<title>Brantock Energy, L.P. – Business Card</title>
<link href="https://fonts.googleapis.com/css2?family=Source+Sans+3:wght@300;400;600&display=swap" rel="stylesheet">
<style>
  :root {
    --orange: #f05a24;
    --ink: #1c1c1c;
    --card: #ffffff;
    --backdrop: #e8e9ea;
    --contact: #fff4ee;
  }
  html, body {
    margin: 0;
    padding: 0;
    width: 1200px;
    height: 1000px;
    overflow: hidden;
    background: var(--backdrop);
  }
  .card {
    position: absolute;
    left: 60px;
    top: 184px;
    width: 1080px;
    height: 632px;
    display: block;
    font-family: "Source Sans 3", "Myriad Pro", sans-serif;
  }
  .card-face { fill: var(--card); }
  .accent { fill: var(--orange); }
  .brand-dot { fill: var(--ink); }
  .brand-name {
    fill: var(--ink);
    font-weight: 600;
  }
  .tagline-frame {
    fill: none;
    stroke: var(--orange);
    stroke-width: 1;
  }
  .tagline {
    fill: var(--orange);
    font-weight: 400;
    font-size: 11px;
    letter-spacing: 0.3px;
  }
  .contact-name {
    fill: var(--contact);
    font-weight: 300;
    font-size: 13px;
  }
  .contact-line {
    fill: var(--contact);
    font-weight: 400;
    font-size: 12.5px;
  }
  .website {
    fill: var(--orange);
    font-weight: 400;
    font-size: 14px;
  }
</style>
</head>
<body>
<svg class="card" viewBox="0 0 596 349" xmlns="http://www.w3.org/2000/svg" aria-label="Brantock Energy business card">
  <rect class="card-face" x="0" y="0" width="596" height="349"/>

  <path class="accent" d="M0,115 C20,55 60,10 105,0 L76,0 C40,15 10,50 0,84 Z"/>

  <path class="accent" d="M403,0 L596,0 L596,289 L391,306 L368,349 L321,349 C280,260 290,80 403,0 Z"/>

  <g class="brand">
    <circle class="brand-dot" cx="66" cy="188" r="22"/>
    <text class="brand-name" x="98" y="186" font-size="28" letter-spacing="1">BRANTOCK</text>
    <text class="brand-name" x="99" y="209" font-size="16" letter-spacing="3">ENERGY L.P.</text>
  </g>

  <g class="tagline-block">
    <rect class="tagline-frame" x="42" y="228" width="224" height="20" rx="2"/>
    <text class="tagline" x="154" y="242" text-anchor="middle">Understanding  |  Solutions  |  Performance</text>
  </g>

  <g class="contact">
    <text class="contact-name" x="323" y="130">Glenda M. Holloway, Principal</text>
    <text class="contact-line" x="341" y="153">Brantock Energy, L.P.</text>
    <text class="contact-line" x="341" y="173">4817 Quimby St.</text>
    <text class="contact-line" x="341" y="193">Houston, TX 77310</text>
    <text class="contact-line" x="341" y="213">phone 713-482-6159</text>
    <text class="contact-line" x="341" y="233">fax 713-624-8841</text>
    <text class="contact-line" x="341" y="253">g.holloway@brantockenergy-example.com</text>
  </g>

  <text class="website" x="590" y="340" text-anchor="end">www.brantockenergy-example.com</text>
</svg>
</body>
</html>
```